Brightpath Works Mobile RV Repair

We are looking for a logo and business cards for a new start up business. We will be doing Mobile RV Repair.
We are in Texas.
I don't have any designs at this point.

Contact Information for Business Card

Emphasis should be on the “Mobile RV Repair” and not so much the name “Brightpath Works”

Requirements
Nice to have
• I like the Mobile RV Repair to cover most of the backside of the card! Not sure on the colors, would like to see it in a few different colors!

```html
<!DOCTYPE html>
<html lang="en">
<head>
<meta charset="utf-8">
<title>Brightpath Works Mobile RV Repair – Business Cards</title>
<link href="https://fonts.googleapis.com/css2?family=Exo+2:wght@200;300;400;600;700&display=swap" rel="stylesheet">
<style>
  :root {
    --backdrop: #565452;
    --card: #1f1f1f;
    --card-edge: #262626;
    --hazard: #f0c419;
    --white: #f2f2f2;
    --accent: #ef6a1a;
    --rule: #d9d9d9;
  }
  * { margin: 0; padding: 0; box-sizing: border-box; }
  html, body { width: 1200px; height: 1200px; overflow: hidden; }
  body {
    background: var(--backdrop);
    font-family: "Exo 2", sans-serif;
    color: var(--white);
    position: relative;
  }
  .card {
    position: absolute;
    left: 243px;
    width: 700px;
    height: 400px;
    border-radius: 18px;
    background: radial-gradient(ellipse at 40% 40%, var(--card-edge), var(--card) 70%);
    overflow: hidden;
  }
  .card--front { top: 170px; }
  .card--back { top: 630px; }

  .hazard-band {
    position: absolute;
    height: 24px;
    background: repeating-linear-gradient(-60deg,
      var(--hazard) 0 26px, transparent 26px 79px);
  }
  .card--front .hazard-band--top { top: 0; left: 145px; right: 0; }
  .card--front .hazard-band--bottom { bottom: 0; left: 0; width: 560px; }
  .card--back .hazard-band--top { top: 0; left: 0; width: 540px; }
  .card--back .hazard-band--bottom { bottom: 0; left: 160px; right: 10px; }

  .front-copy {
    position: absolute;
    left: 0; right: 0;
    top: 122px;
    text-align: center;
  }
  .front-phone {
    font-weight: 700;
    font-size: 76px;
    line-height: 1;
    letter-spacing: 1px;
  }
  .front-service {
    margin-top: 10px;
    font-weight: 200;
    font-size: 66px;
    line-height: 1;
  }
  .front-service .accent { color: var(--accent); font-weight: 300; }

  .brand-mark {
    position: absolute;
    left: 72px; top: 70px;
    width: 176px; height: 120px;
    display: flex; align-items: center; gap: 10px;
  }
  .brand-mark__dot {
    width: 22px; height: 22px; border-radius: 50%;
    background: var(--white); flex: none;
  }
  .brand-mark__name {
    font-weight: 600; font-size: 21px; line-height: 1.1;
  }
  .divider {
    position: absolute;
    left: 309px; top: 57px;
    width: 2px; height: 148px;
    background: var(--rule);
  }
  .business {
    position: absolute;
    left: 347px; top: 50px;
  }
  .business__name {
    font-weight: 700; font-size: 33px; line-height: 1; letter-spacing: .5px;
  }
  .business__tagline {
    margin-top: 6px;
    font-weight: 300; font-size: 21px; letter-spacing: 5.3px;
  }
  .contacts {
    position: absolute;
    left: 347px; top: 146px;
    list-style: none;
    font-weight: 400; font-size: 16px; letter-spacing: .6px;
  }
  .contacts li { display: flex; align-items: center; gap: 10px; height: 24px; margin-bottom: 10px; }
  .contacts svg { width: 22px; height: 22px; flex: none; }

  .fleet-photo {
    position: absolute;
    left: 37px; top: 226px;
    width: 608px; height: 150px;
    border-radius: 6px;
    background: linear-gradient(90deg, #cfc6b0 0%, #b8b6b0 35%, #3d4352 55%, #d6d2c8 75%, #4a4f5d 100%);
  }
</style>
</head>
<body>
  <section class="card card--front" aria-label="Card front">
    <div class="hazard-band hazard-band--top"></div>
    <div class="front-copy">
      <p class="front-phone">210-555-0147</p>
      <p class="front-service">Mobile <span class="accent">RV</span> Repair</p>
    </div>
    <div class="hazard-band hazard-band--bottom"></div>
  </section>

  <section class="card card--back" aria-label="Card back">
    <div class="hazard-band hazard-band--top"></div>
    <div class="brand-mark">
      <span class="brand-mark__dot"></span>
      <span class="brand-mark__name">Brightpath Works</span>
    </div>
    <div class="divider"></div>
    <div class="business">
      <h1 class="business__name">Brightpath Works</h1>
      <p class="business__tagline">MOBILE RV REPAIR</p>
    </div>
    <ul class="contacts">
      <li>
        <svg viewBox="0 0 24 24"><circle cx="12" cy="12" r="12" fill="#f2f2f2"/><path d="M8.2 6.5l2 2.4-1.2 1.5c.8 1.7 2 2.9 3.7 3.7l1.5-1.2 2.4 2-1.1 1.9c-4.3-.3-8-4-8.3-8.3z" fill="#1f1f1f"/></svg>
        <span>210-555-0147</span>
      </li>
      <li>
        <svg viewBox="0 0 24 24"><circle cx="12" cy="12" r="12" fill="#f2f2f2"/><rect x="6.5" y="8" width="11" height="8" rx="1" fill="none" stroke="#1f1f1f" stroke-width="1.6"/><path d="M6.8 8.5L12 12.6l5.2-4.1" fill="none" stroke="#1f1f1f" stroke-width="1.6"/></svg>
        <span>BrightpathWorksRV@postmail.com</span>
      </li>
    </ul>
    <div class="fleet-photo" role="img" aria-label="Photo of a motorhome, a travel trailer and a fifth-wheel camper lined up"></div>
    <div class="hazard-band hazard-band--bottom"></div>
  </section>
</body>
</html>
```